Business Card Design

Copperfield Lantern & Spark, Inc. (CLS), located in Memphis, TN began operating on 2003. We are a certified
minority woman-owned business that genuinely takes a vested interest in our customers. We serve utilities,
government, contractors and end user markets in electrical, water, gas and industrial supplies. Our core
competency as a distributor of electrical materials has positioned us to serve business of all size. As your supply
chain partner, we arm you with the resources you need to make your supply chain more efficient. Our team
works with your team on a daily basis to help you solve problems and achieve goals. This team approach has
helped CLS customers to succeed and we can do the same for you.

NAICS Codes:
423610 Electrical Apparatus and Equipment, Wiring Supplies, and Related Equipment Merchant
Wholesalers
423510 Metal Service Centers and Other Metal Merchant Wholesalers
423720 Plumbing and Heating Equipment and Supplies (Hydronics) Merchant Wholesalers

Certifications
MBE (KRVPQAL, State of Tennessee Up-MRX and FJW), WBE (HQOLT),
WOSB, DOT (TDOT, MDOT, ALDOT, SCDOT, NCDOT, and VDOT), LOSB,
SBE, and LSB Certified
Some of Our Products Include:
. Boxes & Covers
. Conduit & Raceway
. Fittings
. Fuses
. Lamp & Ballasts
. Lighting Controls & Timers
. Lighting Fixtures
. Personal Safety
. Pipes
. Power Distribution
. Terminations Ground & Splices
. Tools & Testers
. Wire, Cords & Cable
. Wiring Devices
. Valves

Industry/Entity Type

Business

Contact Information for Business Card

Marianne T. Holloway - President/CEO
4728 Quillon Ave., Memphis, TN 38127
901-555-0147 office, 901-555-0182 fax, 901-555-0163 cell
mtholloway@clsllc-example.com - www.clsincorp-example.com

```html
<!DOCTYPE html>
<html lang="en">
<head>
<meta charset="utf-8">
<title>Copperfield Lantern &amp; Spark – Business Card</title>
<link href="https://fonts.googleapis.com/css2?family=Open+Sans:wght@400;600&display=swap" rel="stylesheet">
<style>
  :root {
    --page: #e6e4e1;
    --card: #1f1f1f;
    --ink: #f2f2f2;
    --muted: #bdbdbd;
    --accent: #c6c41a;
    --rule: #6a6a6a;
  }
  * { box-sizing: border-box; margin: 0; padding: 0; }
  html, body { width: 1200px; height: 814px; overflow: hidden; }
  body {
    background: var(--page);
    font-family: "Open Sans", Arial, sans-serif;
    color: var(--ink);
    position: relative;
  }
  .card {
    position: absolute;
    top: 258px;
    width: 525px;
    height: 300px;
    background: var(--card);
    border-radius: 3px;
    box-shadow: 0 6px 18px rgba(0,0,0,.25);
    overflow: hidden;
  }
  .card--back { left: 45px; }
  .card--front { left: 630px; }

  /* back */
  .details { position: absolute; left: 26px; top: 24px; width: 440px; font-size: 10.5px; line-height: 1.45; }
  .details h3 { color: var(--accent); font-size: 11px; font-weight: 600; margin-top: 8px; }
  .details h3:first-child { margin-top: 0; }
  .details p { color: var(--ink); }

  /* front */
  .wordmark {
    position: absolute; left: 212px; top: 68px;
    display: flex; align-items: center; gap: 10px;
  }
  .wordmark__dot { width: 14px; height: 14px; border-radius: 50%; background: var(--accent); flex: none; }
  .wordmark__name {
    font-size: 20px; font-weight: 400; color: var(--ink);
    line-height: 1.15; letter-spacing: .5px; text-transform: uppercase;
  }
  .identity {
    position: absolute; right: 300px; top: 150px; text-align: right;
    font-size: 13px; line-height: 1.45; white-space: nowrap;
  }
  .identity__name { color: var(--accent); font-size: 16px; font-weight: 600; margin-bottom: 2px; }
  .divider { position: absolute; left: 240px; top: 158px; width: 1px; height: 108px; background: var(--rule); }
  .contacts { position: absolute; left: 256px; top: 192px; list-style: none; font-size: 13px; line-height: 1.55; }
  .contacts li { display: flex; align-items: center; gap: 8px; }
  .contacts svg { width: 13px; height: 13px; fill: var(--accent); flex: none; }
</style>
</head>
<body>

<section class="card card--back" aria-label="Card back">
  <div class="details">
    <h3>NAICS Codes:</h3>
    <p>423610 Electrical Apparatus &amp; Equipment, Wiring Supplies, &amp; Related Equipment Merchant Wholesalers<br>
    423510 Metal Service Centers &amp; Other Metal Merchant Wholesalers<br>
    423720 Plumbing &amp; Heating Equipment &amp; Supplies (Hydronics) Merchant Wholesalers</p>
    <h3>Certifications:</h3>
    <p>MBE (KRVPQAL, State of Tennessee Up-MRX and FJW), WBE (HQOLT),<br>
    WOSB, DOT (TDOT, MDOT, ALDOT, SCDOT, NCDOT, and VDOT), LOSB,<br>
    SBE &amp; LSB Certified</p>
    <h3>Some of Our Products Include:</h3>
    <p>Boxes &amp; Covers | Conduit &amp; Raceway | Fittings<br>
    Fuses | Lamp &amp; Ballasts | Lighting Controls &amp; Timers | Lighting Fixtures<br>
    Personal Safety | Pipes | Power Distribution | Tools &amp; Testers |<br>
    Wire, Cords &amp; Cable | Terminations Ground &amp; Splices<br>
    Wiring Devices | Valves</p>
  </div>
</section>

<section class="card card--front" aria-label="Card front">
  <div class="wordmark">
    <span class="wordmark__dot"></span>
    <span class="wordmark__name">Copperfield<br>Lantern &amp; Spark</span>
  </div>

  <div class="identity">
    <p class="identity__name">Marianne T. Holloway</p>
    <p>President/CEO</p>
    <p>4728 Quillon Ave.</p>
    <p>Memphis, TN 38127</p>
  </div>

  <span class="divider"></span>

  <ul class="contacts">
    <li><svg viewBox="0 0 16 16" aria-label="Office"><path d="M3 1l3 1 1 3-2 1.5a9 9 0 0 0 4.5 4.5L11 9l3 1 1 3-2 2C7 15 1 9 1 3z"/></svg>901-555-0147</li>
    <li><svg viewBox="0 0 16 16" aria-label="Fax"><path d="M4 1h8v4H4zM1 6h14v7h-3v2H4v-2H1zm4 5v3h6v-3z"/></svg>901-555-0182</li>
    <li><svg viewBox="0 0 16 16" aria-label="Cell"><path d="M4 0h8a1 1 0 0 1 1 1v14a1 1 0 0 1-1 1H4a1 1 0 0 1-1-1V1a1 1 0 0 1 1-1zm1 2v10h6V2z"/></svg>901-555-0163</li>
    <li><svg viewBox="0 0 16 16" aria-label="Email"><path d="M0 3h16v10H0zm1.5 1.5L8 9l6.5-4.5z"/></svg>mtholloway@clsllc-example.com</li>
  </ul>
</section>

</body>
</html>
```